Tolvir Website - endlich neu?!
Aufgabenstellung
Es geht um die Gestaltung der Startseite auf Basis unseres verwendeten Magento-Templates.
Außerdem um die Gestaltung von Visitenkarte und Briefkopf.

```html
<!DOCTYPE html>
<html lang="de">
<head>
<meta charset="utf-8">
<title>Tolvir – Geschäftsausstattung</title>
<link rel="stylesheet" href="https://fonts.googleapis.com/css2?family=Arimo:wght@400;700&display=swap">
<style>
  :root {
    --bg: #dcdcdc;
    --paper: #ffffff;
    --panel: #d6d6d6;
    --panel-light: #e4e4e4;
    --ink: #111111;
    --muted: #555555;
    --accent: #e3161b;
    --line: #222222;
  }
  * { box-sizing: border-box; margin: 0; padding: 0; }
  html, body { width: 1200px; height: 1030px; overflow: hidden; }
  body { background: var(--bg); font-family: "Arimo", Arial, sans-serif; color: var(--ink); position: relative; }

  .brand-name { font-family: "Arimo", Arial, sans-serif; font-weight: 700; color: var(--ink); letter-spacing: 0.5px; line-height: 1; }
  .claim { color: var(--muted); text-transform: uppercase; letter-spacing: 1px; line-height: 1.15; }

  /* Sticker */
  .sticker { position: absolute; left: 257px; top: 278px; width: 160px; height: 130px; background: var(--paper); border-radius: 50%; display: flex; align-items: center; justify-content: center; }
  .sticker .brand-name { font-size: 34px; }

  /* Cards */
  .card { position: absolute; width: 350px; height: 222px; overflow: hidden; }
  .card-front { left: 73px; top: 462px; background: var(--panel); }
  .card-front .halo { position: absolute; left: 120px; top: 8px; width: 190px; height: 160px; border-radius: 50%; background: var(--paper); display: flex; align-items: center; justify-content: center; }
  .card-front .brand-name { font-size: 44px; }
  .card-front .claim { position: absolute; right: 24px; bottom: 22px; font-size: 10px; text-align: right; }

  .card-back { left: 73px; top: 720px; background: var(--panel-light); }
  .card-back svg { position: absolute; inset: 0; }
  .card-back .claim { position: absolute; left: 44px; bottom: 22px; font-size: 10px; }
  .contact { position: absolute; right: 22px; top: 22px; text-align: right; font-weight: 700; font-size: 11.5px; line-height: 1.35; color: #222; }
  .contact .person { color: var(--accent); font-size: 12.5px; letter-spacing: 0.6px; text-transform: uppercase; margin-bottom: 18px; }
  .contact .block { margin-bottom: 14px; }

  /* Letterhead */
  .letter { position: absolute; left: 505px; top: 68px; width: 610px; height: 862px; background: var(--paper); overflow: hidden; }
  .letter svg { position: absolute; inset: 0; }
  .letter-brand { position: absolute; right: 46px; top: 92px; display: flex; flex-direction: column; align-items: flex-end; }
  .letter-brand .brand-name { font-size: 30px; }
  .letter-brand .claim { font-size: 6.5px; text-align: right; margin-top: 58px; }
  .recipient { position: absolute; left: 72px; top: 190px; font-size: 11px; line-height: 1.5; }
  .letter-body { position: absolute; left: 76px; top: 338px; width: 440px; font-size: 10.5px; line-height: 1.5; }
  .letter-body .subject { font-weight: 700; }
  .letter-body p { margin-bottom: 14px; }
  .letter-body .greeting { margin-bottom: 14px; }
  .letter-footer { position: absolute; left: 96px; right: 40px; bottom: 44px; display: flex; justify-content: space-between; font-size: 7.5px; line-height: 1.7; }
  .letter-footer strong { font-weight: 700; }
  .bank { display: grid; grid-template-columns: 36px auto; }
  .bank strong { grid-column: 1 / 3; }
</style>
</head>
<body>

  <div class="sticker">
    <span class="brand-name">Tolvir</span>
  </div>

  <div class="card card-front">
    <div class="halo"><span class="brand-name">Tolvir</span></div>
    <div class="claim">Kleidung,<br>die länger passt</div>
  </div>

  <div class="card card-back">
    <svg width="350" height="222" viewBox="0 0 350 222" aria-hidden="true">
      <path d="M185,0 Q150,110 235,222 L350,222 L350,0 Z" fill="var(--paper)"/>
      <path d="M185,0 Q150,110 235,222" fill="none" stroke="var(--line)" stroke-width="1.5"/>
    </svg>
    <div class="claim">Kleidung,<br>die länger passt</div>
    <div class="contact">
      <div class="person">Lena Harwick</div>
      <div class="block">Kastanienweg 14<br>30159 Lindenfeld</div>
      <div class="block">Fon (0412) 55 310 620<br>Fax (0412) 55 310 621</div>
      <div>Lena@Tolvir.de<br>www.Tolvir.de</div>
    </div>
  </div>

  <div class="letter">
    <svg width="610" height="862" viewBox="0 0 610 862" aria-hidden="true">
      <rect width="610" height="862" fill="var(--panel-light)"/>
      <circle cx="545" cy="235" r="85" fill="#eeeeee"/>
      <path d="M0,150 C210,40 560,80 610,470 L610,862 L0,862 Z" fill="var(--paper)"/>
      <path d="M0,150 C210,40 560,80 610,470" fill="none" stroke="#777" stroke-width="1"/>
    </svg>
    <div class="letter-brand">
      <span class="brand-name">Tolvir</span>
      <div class="claim">Kleidung,<br>die länger passt</div>
    </div>
    <div class="recipient">Herr Mustermann<br>Musterstraße 22<br>40022 Musterhausen</div>
    <div class="letter-body">
      <div class="greeting"><span class="subject">Corporate Design für Tolvir</span><br>Sehr geehrte Frau Mustermann,</div>
      <p>herzlichen Dank für die Logos. Die Logik der Logos ist logisch und ich komme zu der logischen Endlogik, dass ich die Qual der Wahl habe. Der Briefbogen oder das Briefpapier oder der Kopfbogen ist ein ein- oder beidseitig vorgedruckter Formatpapierbogen für die private oder geschäftliche briefliche Korrespondenz, dem individuell ein Text und/oder Daten hinzugefügt werden müssen. Der Briefbogen dient der Arbeitsvereinfachung im Büro und der Corporate Identity des Absenders. Der Briefbogen ist ein endbeschnittenes und ausgerüstetes Rohprodukt. Briefbogen bestehen in der Regel aus besserem Schreib- oder Kopierpapier mit einem zuvor in einem beliebigen Druckverfahren aufgebrachten Briefkopf, der meist relevante Absenderangaben enthält.</p>
      <p>Das Geschäftsbriefpapier enthält typischerweise folgende Absenderangaben: den Unternehmensnamen mit Rechtsform, die Postanschrift, die Kommunikationsdaten (zum Beispiel Telefonnummer, E-Mail-Adresse und Telefax), ein Logo (falls üblich), ein reserviertes Feld für die Empfängeranschrift, eine Referenzzeile.</p>
      <p>Mit freundlichem Gruß</p>
      <p>Martina Musterfrau</p>
    </div>
    <div class="letter-footer">
      <div><strong>Tolvir</strong><br>Kastanienweg 14<br>30159 Lindenfeld</div>
      <div>Fon (0412) 55 310 620<br>Fax (0412) 55 310 621<br>Lena@Tolvir.de</div>
      <div class="bank"><strong>Nordstadt Bank</strong><span>BLZ</span><span>240 118 30</span><span>Kto.</span><span>41 207 356</span></div>
      <div class="bank"><strong>Kreiskasse Eldorf</strong><span>BLZ</span><span>240 118 30</span><span>Kto.</span><span>41 207 356</span></div>
    </div>
  </div>

</body>
</html>
```